Waste Oil Filter collection & disposal

Basically I need a 1 page website for the business called Grennick Waste Partners.
We are a environmental service provider and we collect and dispose of waste oil filters to protect the environment from hazardous waste oil products.

This is the link to our current website: www.grennickwaste.co.nz

we want it to look fresh and better than our current website. we may potentially look at getting a new logo designed and are open to ideas/designs if you have any.

Industry/Entity Type

Business

Logo Text

Grennick Waste Partners

Number of Pages Required

1 page

Requirements
Must have
• same colours as current website.
• description of what service we provide please refer to leaflet attached

```html
<!DOCTYPE html>
<html lang="en">
<head>
<meta charset="utf-8">
<title>Grennick Waste Partners Ltd</title>
<link href="https://fonts.googleapis.com/css2?family=Questrial&display=swap" rel="stylesheet">
<style>
:root{
  --navy:#17497a;
  --navy-deep:#123e69;
  --navy-foot:#0e365c;
  --green:#629766;
  --grey-band:#eeeced;
  --grey-box:#f0eff0;
  --circle:#cfcfcf;
  --text:#333;
  --muted:#666;
  --white:#fff;
}
*{box-sizing:border-box;margin:0;padding:0}
html,body{width:1200px;height:2871px;overflow:hidden}
body{position:relative;font-family:"Questrial",Arial,sans-serif;color:var(--text);background:var(--white)}
.abs{position:absolute}
/* header */
.topline{left:0;top:0;width:1200px;height:5px;background:var(--navy)}
.header{left:0;top:5px;width:1200px;height:79px;background:var(--white)}
.brand{left:86px;top:24px;display:flex;align-items:center;gap:10px;font-size:17px;color:var(--navy);font-weight:400}
.brand-mark{width:22px;height:22px;background:var(--green)}
.info{top:22px;font-size:14px;color:#444;display:flex;align-items:center;gap:9px}
.nav{top:60px;font-size:13px;letter-spacing:.5px;color:#222}
.nav-sep{top:58px;width:1px;height:18px;background:#bbb}
.callbox{left:909px;top:0;width:291px;height:80px;background:var(--navy);color:var(--white);text-align:center;padding-top:12px}
.callbox .label{font-size:19px;letter-spacing:.5px}
.callbox .phone{font-size:26px;font-weight:700;margin-top:4px;letter-spacing:1px}
/* hero */
.hero{left:0;top:84px;width:1200px;height:597px;background:linear-gradient(180deg,#7c7a6a 0%,#b9a276 22%,#8d8a7c 42%,#6e6f6c 65%,#7d7873 100%)}
.hero-panel{left:264px;top:272px;width:670px;height:229px;background:rgba(40,40,40,.35)}
.hero-title{left:0;top:322px;width:1200px;text-align:center;font-size:42px;color:var(--white)}
.hero-rule{left:520px;top:390px;width:160px;height:2px;background:#3c8fd3}
.hero-sub{left:0;top:406px;width:1200px;text-align:center;font-size:22px;line-height:38px;color:var(--white)}
/* about */
.about-box{left:82px;top:1003px;width:381px;height:103px;background:var(--grey-box)}
.about-photo{left:165px;top:760px;width:486px;height:310px;background:linear-gradient(135deg,#2b3037,#4a5663 55%,#2b8ac4 80%,#1f2a33)}
.counter{left:100px;top:1026px;font-size:44px;color:#333}
.counter small{font-size:24px}
.updown{left:103px;width:36px;height:36px}
.about-title{left:697px;top:776px;width:413px;text-align:center;font-size:38px;letter-spacing:1px;color:#222}
.about-rule{left:853px;top:840px;width:100px;height:1px;background:#999}
.about-text{left:697px;top:864px;width:413px;font-size:14.5px;line-height:24.5px;text-align:justify;color:#555}
.btn-solid{left:835px;top:1014px;width:137px;height:42px;background:var(--navy);color:var(--white);font-size:14px;display:flex;align-items:center;justify-content:center;letter-spacing:.5px}
/* process */
.process{left:0;top:1208px;width:1200px;height:392px;background:var(--grey-band)}
.process-tag{left:469px;top:1177px;width:262px;height:79px;background:var(--navy);border:3px solid var(--white);box-shadow:0 0 0 1px #ccc;color:var(--white);font-size:27px;display:flex;align-items:center;justify-content:center;letter-spacing:.5px}
.step{width:264px;text-align:center}
.step-circle{width:130px;height:130px;border-radius:50%;background:var(--circle);margin:0 auto;display:flex;align-items:center;justify-content:center}
.step-label{font-size:24px;color:#333;margin-top:23px}
.btn-line{display:inline-block;margin-top:12px;width:105px;height:35px;border:1px solid var(--navy);font-size:11.5px;line-height:33px;color:#333;letter-spacing:.3px}
.step-arrow{top:1366px}
/* gallery */
.tile{width:237px;height:173px}
/* quote */
.quote{left:80px;top:2182px;width:1028px;height:128px;background:var(--green)}
.avatar{left:120px;top:2158px;width:136px;height:136px;border-radius:50%;border:4px solid var(--white);background:linear-gradient(160deg,#e6b43a,#c98f58 55%,#7a5a44)}
.quote-text{left:295px;top:2212px;font-size:23px;color:var(--white)}
.quote-src{left:300px;top:2256px;font-size:13px;color:#1f3d25;letter-spacing:.5px}
/* contact */
.contact{left:0;top:2325px;width:1200px;height:475px;background:var(--navy)}
.req{left:86px;top:2393px;font-size:34px;line-height:50px;color:var(--white);letter-spacing:.5px}
.req .hl{color:#8fc98a}
.req-rule{left:86px;top:2505px;width:115px;height:1px;background:#9fb6cf}
.req-text{left:86px;top:2524px;font-size:18.5px;line-height:33px;color:var(--white)}
.infobox{left:86px;top:2622px;width:494px;height:128px;background:var(--navy-deep)}
.info-col{top:2652px;font-size:14px;line-height:22px;color:#dfe8f2}
.info-col b{font-weight:400;color:var(--white);font-size:14.5px;letter-spacing:.5px}
.info-div{left:340px;top:2640px;width:1px;height:92px;background:#3e6690}
.col-div{left:612px;top:2385px;width:1px;height:390px;background:#345f8a}
.field{border:1px solid #c9d6e4;color:#dfe8f2;font-size:13px;padding:0 20px;display:flex;align-items:center}
.submit{left:653px;top:2704px;width:459px;height:46px;background:var(--green);color:var(--white);font-size:19px;display:flex;align-items:center;justify-content:center;letter-spacing:.5px}
.footer{left:0;top:2800px;width:1200px;height:71px;background:var(--navy-foot);color:#cfd9e4;font-size:11px;text-align:center;line-height:71px}
</style>
</head>
<body>
<div class="abs topline"></div>
<header class="abs header"></header>
<div class="abs brand"><span class="brand-mark"></span>Grennick Waste Partners Ltd</div>
<div class="abs info" style="left:454px">
  <svg width="16" height="12" viewBox="0 0 16 12"><rect width="16" height="12" rx="1" fill="#17497a"/><path d="M1 1l7 6 7-6" stroke="#fff" stroke-width="1.4" fill="none"/></svg>
  info@grennickwaste.co.nz</div>
<div class="abs info" style="left:676px">
  <svg width="16" height="16" viewBox="0 0 16 16"><circle cx="8" cy="8" r="8" fill="#17497a"/><path d="M8 3.5V8h3.5" stroke="#fff" stroke-width="1.5" fill="none"/></svg>
  Mon-Fri 7.30 am - 5.00 pm</div>
<nav>
  <span class="abs nav" style="left:352px">HOMEPAGE</span>
  <span class="abs nav-sep" style="left:460px"></span>
  <span class="abs nav" style="left:496px">MY GALLERY</span>
  <span class="abs nav-sep" style="left:613px"></span>
  <span class="abs nav" style="left:649px">SERVICES</span>
  <span class="abs nav-sep" style="left:745px"></span>
  <span class="abs nav" style="left:781px">CONTACT US</span>
</nav>
<div class="abs callbox"><div class="label">CALL US TODAY!</div><div class="phone">06 555 0142</div></div>

<section>
  <div class="abs hero" role="img" aria-label="Landfill heaped with discarded plastic bottles and containers under a sunset sky"></div>
  <div class="abs hero-panel"></div>
  <h1 class="abs hero-title" style="font-weight:400">Grennick Waste Partners Ltd</h1>
  <div class="abs hero-rule"></div>
  <p class="abs hero-sub">service the Lower North Island and specialise in the<br>collection &amp; disposal of oil &amp; fuel filters</p>
</section>

<section>
  <div class="abs about-box"></div>
  <div class="abs about-photo" role="img" aria-label="Blue waste bin with crumpled paper on a desk in front of a person in a suit"></div>
  <svg class="abs updown" style="top:862px" viewBox="0 0 36 36"><circle cx="18" cy="18" r="16.5" fill="none" stroke="#bbb" stroke-width="1.5"/><path d="M18 26V10M12 16l6-6 6 6" stroke="#bbb" stroke-width="1.5" fill="none"/></svg>
  <svg class="abs updown" style="top:918px" viewBox="0 0 36 36"><circle cx="18" cy="18" r="16.5" fill="none" stroke="#bbb" stroke-width="1.5"/><path d="M18 10v16M12 20l6 6 6-6" stroke="#bbb" stroke-width="1.5" fill="none"/></svg>
  <div class="abs counter">3<small>/4</small></div>
  <h2 class="abs about-title" style="font-weight:400">ABOUT US</h2>
  <div class="abs about-rule"></div>
  <p class="abs about-text">Lorem Ipsum is simply dummy text of the printing and typesetting industry. Lorem Ipsum has been the industry's standard dummy text ever since the 1500s, when an unknown printer took a galley of type and scrambled it to make a type specimen book.</p>
  <div class="abs btn-solid">LEARN MORE</div>
</section>

<section>
  <div class="abs process"></div>
  <h2 class="abs process-tag" style="font-weight:400">THE PROCESS</h2>
  <svg class="abs" style="left:37px;top:1356px" width="48" height="48" viewBox="0 0 48 48"><circle cx="24" cy="24" r="22" fill="none" stroke="#ddd" stroke-width="2"/><path d="M34 24H14M21 17l-7 7 7 7" stroke="#ddd" stroke-width="2" fill="none"/></svg>
  <svg class="abs" style="left:1119px;top:1356px" width="48" height="48" viewBox="0 0 48 48"><circle cx="24" cy="24" r="22" fill="none" stroke="#ddd" stroke-width="2"/><path d="M14 24h20M27 17l7 7-7 7" stroke="#ddd" stroke-width="2" fill="none"/></svg>

  <div class="abs step" style="left:69px;top:1315px">
    <div class="step-circle"><svg width="48" height="30" viewBox="0 0 48 30"><path d="M4 4h12l-4 22H0zM19 4h12l-4 22H15zM34 4h14l-4 22H30z" fill="#666"/></svg></div>
    <div class="step-label">Drained</div><span class="btn-line">LEARN MORE</span></div>
  <div class="abs step" style="left:333px;top:1315px">
    <div class="step-circle"><svg width="44" height="44" viewBox="0 0 44 44"><circle cx="22" cy="22" r="21" fill="#666"/><path d="M12 24a10 10 0 0 1 17-8l3-3v10h-10l4-4a6 6 0 0 0-10 5zM32 20a10 10 0 0 1-17 8l-3 3V21h10l-4 4a6 6 0 0 0 10-5z" fill="#cfcfcf"/></svg></div>
    <div class="step-label">Sorted</div><span class="btn-line">LEARN MORE</span></div>
  <div class="abs step" style="left:597px;top:1315px">
    <div class="step-circle"><svg width="44" height="44" viewBox="0 0 44 44"><circle cx="22" cy="22" r="20" fill="#666"/><path d="M14 8v28M22 4v36M30 8v28" stroke="#cfcfcf" stroke-width="3"/></svg></div>
    <div class="step-label">Drained again</div><span class="btn-line">LEARN MORE</span></div>
  <div class="abs step" style="left:861px;top:1315px">
    <div class="step-circle"><svg width="48" height="40" viewBox="0 0 48 40"><g fill="#666"><rect x="0" y="0" width="22" height="8"/><rect x="26" y="0" width="22" height="8"/><rect x="0" y="11" width="10" height="8"/><rect x="13" y="11" width="22" height="8"/><rect x="38" y="11" width="10" height="8"/><rect x="0" y="22" width="22" height="8"/><rect x="26" y="22" width="22" height="8"/><rect x="0" y="33" width="10" height="7"/><rect x="13" y="33" width="22" height="7"/><rect x="38" y="33" width="10" height="7"/></g></svg></div>
    <div class="step-label">Crushed into bricks</div><span class="btn-line">LEARN MORE</span></div>

  <svg class="abs step-arrow" style="left:311px" width="44" height="28" viewBox="0 0 44 28"><path d="M2 14h38M28 3l12 11-12 11" stroke="#bbb" stroke-width="2.5" fill="none"/></svg>
  <svg class="abs step-arrow" style="left:575px" width="44" height="28" viewBox="0 0 44 28"><path d="M2 14h38M28 3l12 11-12 11" stroke="#bbb" stroke-width="2.5" fill="none"/></svg>
  <svg class="abs step-arrow" style="left:839px" width="44" height="28" viewBox="0 0 44 28"><path d="M2 14h38M28 3l12 11-12 11" stroke="#bbb" stroke-width="2.5" fill="none"/></svg>
</section>

<section>
  <div class="abs tile" style="left:86px;top:1684px;background:linear-gradient(135deg,#c9d6e2,#e8ecef 50%,#4d7fae)" role="img" aria-label="Workers in protective suits sorting waste at a recycling plant"></div>
  <div class="abs tile" style="left:348px;top:1684px;background:linear-gradient(135deg,#3b2a2e,#7a3d5c 45%,#4a6a3a)" role="img" aria-label="Person emptying a colander of scraps into a compost bin"></div>
  <div class="abs tile" style="left:612px;top:1684px;background:linear-gradient(135deg,#7a1414,#c62a26 50%,#5a0f0f)" role="img" aria-label="Red painted metal sign reading waste"></div>
  <div class="abs tile" style="left:875px;top:1684px;background:linear-gradient(135deg,#d23a3a,#e6c64a 40%,#3d8fd0 70%,#a7b5b8)" role="img" aria-label="Pile of colourful cans and plastic packaging"></div>
  <div class="abs tile" style="left:86px;top:1880px;background:linear-gradient(135deg,#b84a3a,#d6944c 50%,#8a7a6a)" role="img" aria-label="Stacked bales of compressed recycled cans in a warehouse"></div>
  <div class="abs tile" style="left:348px;top:1880px;background:linear-gradient(135deg,#e8c77a,#9fbf7a 50%,#2f6a9a)" role="img" aria-label="Hand dropping a plastic bottle into a recycling bin"></div>
  <div class="abs tile" style="left:612px;top:1880px;background:linear-gradient(135deg,#3e4a3a,#8a8a7a 50%,#4a4f55)" role="img" aria-label="Rubbish dumped beside the road near parked cars"></div>
  <div class="abs tile" style="left:875px;top:1880px;background:linear-gradient(180deg,#a9c9e8,#6a9a5a 55%,#4a5a4a)" role="img" aria-label="Green waste collection truck on a road"></div>
</section>

<section>
  <div class="abs quote"></div>
  <div class="abs avatar" role="img" aria-label="Portrait of a smiling worker in a yellow hard hat"></div>
  <p class="abs quote-text">One litre of used oil can contaminate one million litres of water ............</p>
  <p class="abs quote-src">HARBOURSIDE CITY COUNCIL</p>
</section>

<section>
  <div class="abs contact"></div>
  <h2 class="abs req" style="font-weight:400">REQUEST<br>FREE <span class="hl">APPOINTMENT!</span></h2>
  <div class="abs req-rule"></div>
  <p class="abs req-text">We are available to help you every step of the way<br>with your construction project.</p>
  <div class="abs infobox"></div>
  <svg class="abs" style="left:106px;top:2650px" width="20" height="24" viewBox="0 0 20 24"><path d="M10 1a8 8 0 0 0-8 8c0 6 8 14 8 14s8-8 8-14a8 8 0 0 0-8-8z" fill="none" stroke="#3f7bb8" stroke-width="1.6"/><circle cx="10" cy="9" r="3" fill="none" stroke="#3f7bb8" stroke-width="1.6"/></svg>
  <div class="abs info-col" style="left:146px"><b>LOCATION</b><br>45 RIVERSIDE ROAD,<br>PALMERSTON 4410</div>
  <div class="abs info-div"></div>
  <svg class="abs" style="left:360px;top:2650px" width="20" height="22" viewBox="0 0 20 22"><rect x="1" y="1" width="18" height="20" rx="2" fill="none" stroke="#3f7bb8" stroke-width="1.6"/><path d="M6 6c0 6 3 9 8 10l1-3-3-1-1 1c-1-1-2-2-2-4l1-1-1-3z" fill="#3f7bb8"/></svg>
  <div class="abs info-col" style="left:402px"><b>CONTACTS</b><br>06 555 0142<br>info@grennickwaste.co.nz</div>
  <div class="abs col-div"></div>
  <div class="abs field" style="left:653px;top:2410px;width:459px;height:46px">Name...</div>
  <div class="abs field" style="left:653px;top:2481px;width:214px;height:47px">Email...</div>
  <div class="abs field" style="left:900px;top:2481px;width:212px;height:47px">Phone No...</div>
  <div class="abs field" style="left:653px;top:2553px;width:459px;height:127px;align-items:flex-start;padding-top:16px">Massege...</div>
  <div class="abs submit">SUBMIT</div>
</section>

<footer class="abs footer">Powered by Brightleaf © 2017</footer>
</body>
</html>
```